Flyer Design for Exciting Fundraising Personalised Medal Hangers

We are a small Aussie business, Brightmark, who are interested in having a colourful flyer designed to promote our personalised medal hangers. We wish to show a quality product which will be fun and exciting for club members. People should be proud to display their hard earned awards.

Business information:
Brightmark
(07) 4629 3057
info@brightmark-example.com.au
www.brightmark-example.com.au

Target Market(s)

Mums, sports clubs, dance clubs

Industry/Entity Type

Club

Requirements
Must have
• Fundraiser
• Unique
• Personalised
• 25% of proceeds to your club
• From just $30
• Choice of Size
• Choice of Colour
• Choice of Images
• Add Extensions
• Traditional fundraiser or Easy Online order
• Images attached of 'Medal Hanger Double/Triple/Quadruple' can be used if possible. Even if just 1 of the 3 images are used to show we can add extensions.
Nice to have
• I'd just like something colourful and eye catching. Do you have your own sporting medals? Would you like a fun and colourful personalised way to display them?

```html
<!DOCTYPE html>
<html lang="en">
<head>
<meta charset="utf-8">
<title>Medal Hanger Fundraiser – Brightmark</title>
<link rel="stylesheet" href="https://fonts.googleapis.com/css2?family=Amatic+SC:wght@400;700&family=Londrina+Solid:wght@300;400&display=swap">
<style>
  :root {
    --teal: #6fadaa;
    --teal-light: #8fc4b1;
    --cream: #f6f1cc;
    --board: #f4efcf;
    --magenta: #a3174f;
    --mustard: #e5b42c;
    --plum: #5a1f55;
    --navy: #1d3a5c;
    --brand-teal: #2aa3bb;
    --frame: #f3efd0;
    --ribbon-plum: rgba(120, 30, 80, 0.35);
    --ribbon-orange: rgba(233, 150, 40, 0.35);
    --ribbon-olive: rgba(110, 140, 60, 0.35);
    --silhouette: rgba(236, 232, 205, 0.6);
  }
  html, body {
    margin: 0;
    padding: 0;
    overflow: hidden;
    background: #ffffff;
  }
  .flyer {
    position: relative;
    width: 1200px;
    height: 810px;
    overflow: hidden;
    font-family: "Amatic SC", cursive;
  }
  .chevron-field {
    position: absolute;
    inset: 0;
    background: linear-gradient(160deg, var(--teal-light) 0%, var(--teal) 100%);
  }
  .frame {
    position: absolute;
    left: 32px;
    top: 27px;
    width: 1133px;
    height: 770px;
    border: 3px solid var(--frame);
    box-sizing: border-box;
  }
  .title-disc {
    position: absolute;
    left: 313px;
    top: -439px;
    width: 808px;
    height: 808px;
    border-radius: 50%;
    background: var(--cream);
  }
  .title {
    position: absolute;
    left: 313px;
    width: 808px;
    margin: 0;
    text-align: center;
  }
  .title-main {
    top: 24px;
    font-family: "Londrina Solid", sans-serif;
    font-weight: 300;
    font-size: 100px;
    line-height: 1;
    letter-spacing: 3px;
    color: var(--magenta);
  }
  .title-sub {
    top: 124px;
    font-family: "Amatic SC", cursive;
    font-size: 110px;
    font-weight: 400;
    line-height: 1;
    letter-spacing: 8px;
    color: var(--mustard);
  }
  .garland {
    position: absolute;
    left: 372px;
    top: 140px;
    width: 690px;
    height: 230px;
  }
  .brand {
    position: absolute;
    left: 648px;
    top: 266px;
    display: flex;
    align-items: center;
    gap: 8px;
    font-family: "Amatic SC", cursive;
    font-weight: 700;
    font-size: 40px;
    line-height: 1;
    color: var(--brand-teal);
  }
  .brand-dot {
    width: 16px;
    height: 16px;
    border-radius: 50%;
    background: var(--brand-teal);
  }
  .hanger {
    position: absolute;
    background:
      linear-gradient(180deg, var(--board) 0%, var(--board) var(--board-end), transparent var(--board-end)),
      linear-gradient(90deg, var(--ribbon-plum) 0%, rgba(40,110,190,0.3) 22%, transparent 32%, transparent 58%, var(--ribbon-orange) 68%, var(--ribbon-plum) 84%, var(--ribbon-olive) 100%);
    border-radius: 3px;
  }
  .hanger-double { left: 58px; top: 50px;  width: 240px; height: 176px; --board-end: 46%; }
  .hanger-triple { left: 54px; top: 238px; width: 248px; height: 212px; --board-end: 54%; }
  .hanger-quad   { left: 61px; top: 463px; width: 222px; height: 204px; --board-end: 63%; }
  .proceeds {
    position: absolute;
    left: 358px;
    top: 446px;
    width: 736px;
    height: 69px;
    border-radius: 14px;
    background: var(--cream);
    display: flex;
    align-items: center;
    justify-content: center;
    margin: 0;
    font-family: "Londrina Solid", sans-serif;
    font-weight: 300;
    font-size: 60px;
    letter-spacing: 2px;
    color: var(--plum);
  }
  .tagline {
    position: absolute;
    left: 290px;
    top: 600px;
    width: 620px;
    margin: 0;
    text-align: center;
    font-family: "Londrina Solid", sans-serif;
    font-weight: 300;
    font-size: 27px;
    line-height: 48px;
    letter-spacing: 2px;
    color: var(--navy);
  }
  .pointer {
    position: absolute;
    left: 895px;
    top: 605px;
    width: 235px;
    height: 70px;
  }
  .athletes {
    position: absolute;
    left: 63px;
    top: 708px;
    width: 1080px;
    height: 82px;
    background:
      linear-gradient(180deg, transparent 0%, var(--silhouette) 25%, var(--silhouette) 80%, transparent 100%);
    -webkit-mask: linear-gradient(90deg, transparent 0%, #000 6%, #000 94%, transparent 100%);
    mask: linear-gradient(90deg, transparent 0%, #000 6%, #000 94%, transparent 100%);
  }
</style>
</head>
<body>
<main class="flyer">
  <div class="chevron-field" role="img" aria-label="Teal and mint zig-zag chevron background pattern"></div>
  <div class="frame"></div>

  <div class="title-disc"></div>
  <h1 class="title title-main">MEDAL HANGER</h1>
  <h2 class="title title-sub">FUNDRAISER</h2>

  <svg class="garland" viewBox="0 0 690 230" role="img" aria-label="Leafy vine garland curving under the title">
    <path d="M10 12 Q345 418 680 12" fill="none" stroke="var(--navy)" stroke-width="3"/>
  </svg>

  <div class="brand"><span class="brand-dot"></span><span>Brightmark</span></div>

  <div class="hanger hanger-double" role="img" aria-label="Double personalised medal hanger with colourful ribboned medals"></div>
  <div class="hanger hanger-triple" role="img" aria-label="Triple personalised medal hanger with colourful ribboned medals"></div>
  <div class="hanger hanger-quad" role="img" aria-label="Quadruple personalised medal hanger with colourful ribboned medals"></div>

  <p class="proceeds">25% PROCEEDS TO YOUR CLUB</p>

  <p class="tagline">UNIQUE AND EXCITING FUNDRAISER TO<br>PROUDLY DISPLAY YOUR HARD-EARNED MEDALS!</p>

  <svg class="pointer" viewBox="0 0 235 70" aria-hidden="true">
    <path d="M4 24 Q120 16 228 26" fill="none" stroke="var(--navy)" stroke-width="3" stroke-linecap="round"/>
    <path d="M205 4 L228 26 L212 62" fill="none" stroke="var(--navy)" stroke-width="3" stroke-linecap="round" stroke-linejoin="round"/>
  </svg>

  <div class="athletes" role="img" aria-label="Row of pale sport and dance silhouettes: cricket, running, dance, gymnastics, horse riding, cheerleading"></div>
</main>
</body>
</html>
```